Nutritional Supplement Products Label

We need a label design for a nutritional supplement product line. The product line name is Lumorra and the tagline is "the cleanest nutritional supplement on the planet". Therefore the label needs to be clean, professional and not overly done. It also needs to communicate a revived life and renewed health if possible. I have attached a word document with more details.
Target Market(s)
Primarily women ages 30-50. Professional women and stay at home mothers. The healthy minded mothers (and men).
Industry/Entity Type
Health
Look and feel

```html
<!DOCTYPE html>
<html lang="en">
<head>
<meta charset="utf-8">
<title>Lumorra Vita-Restore Label</title>
<link href="https://fonts.googleapis.com/css2?family=Lato:wght@400;700;900&family=Archivo+Black&display=swap" rel="stylesheet">
<style>
:root{
  --blue:#1f9ad6;
  --green:#7cbd3a;
  --ink:#333;
  --grey:#5a5a5a;
  --bg:#e9e9e9;
  --label:#ffffff;
  --flag-red:#c8313e;
  --flag-blue:#2b3f8c;
}
*{margin:0;padding:0;box-sizing:border-box}
html,body{width:1079px;height:1200px;overflow:hidden;background:var(--bg);font-family:"Lato",Arial,sans-serif;color:var(--ink)}
.label{position:absolute;left:0;top:400px;width:1079px;height:400px;background:var(--label)}
.band{position:absolute;left:0;width:100%;height:6px}
.band.g1{top:0;background:var(--green)}
.band.b1{top:9px;background:var(--blue)}
.band.b2{bottom:10px;background:var(--blue)}
.band.g2{bottom:2px;background:var(--green)}

.usage{position:absolute;left:53px;top:30px;width:232px}
.usage h2{color:var(--blue);font-size:15px;font-weight:700;margin-bottom:14px}
.usage p{font-size:8.8px;line-height:11px;color:var(--grey)}
.usage .note{border:1.5px solid var(--green);padding:5px 8px;margin:14px 0 18px 4px;width:218px;text-align:justify}
.badges{position:absolute;left:12px;top:306px;display:flex}
.badge{width:76px;text-align:center;font-size:9.5px;color:var(--grey);white-space:nowrap}
.badge .mark{width:50px;height:50px;margin:0 auto 8px;border-radius:50%;border:2px solid #b9b9b9;background:#f2f2f2}
.badge .mark.sq{border-radius:4px}

.brand-name{position:absolute;left:380px;top:38px;width:340px;text-align:center;font-size:54px;font-weight:900;color:var(--blue);letter-spacing:1px;line-height:64px}
.sun{position:absolute;left:495px;top:128px;width:130px;height:95px;border-radius:50%;background:radial-gradient(circle,#f4a51c 0%,#f9c93a 45%,rgba(255,230,120,0) 72%)}
.product{position:absolute;left:380px;top:220px;width:340px;text-align:center}
.product h1{font-size:40px;font-weight:700;color:var(--blue);line-height:42px}
.product .sub{font-size:22px;color:var(--green);line-height:24px}
.product .desc{font-size:14.5px;color:var(--grey);line-height:16px;margin-top:14px}
.pill{display:inline-block;margin-top:13px;background:var(--blue);color:#fff;font-size:13px;padding:4px 18px;letter-spacing:.2px}

.facts{position:absolute;left:832px;top:26px;width:216px;border:3px solid var(--green);padding:2px;background:#fff}
.facts .inner{border:2px solid #000;padding:3px 4px 3px}
.facts h3{font-family:"Archivo Black",Arial,sans-serif;font-size:15px;letter-spacing:2.4px;line-height:17px}
.facts .serv{font-size:7.6px;line-height:9px;border-bottom:5px solid #000;padding-bottom:2px}
.facts table{width:100%;border-collapse:collapse;font-size:7.8px}
.facts td{border-bottom:.6px solid #000;padding:.6px 0;line-height:9px}
.facts td.n{text-align:right;padding-right:4px}
.facts td.p{text-align:right;width:30px}
.facts .hd td{font-size:7.4px}
.facts .b{font-weight:700}
.facts .in{padding-left:10px}
.facts .thick td{border-bottom:4px solid #000}
.facts small{font-size:5.5px}
.facts .foot{font-size:6.3px;line-height:8px;padding-top:3px}

.origin{position:absolute;left:882px;top:317px;width:56px;text-align:center;font-size:8px;line-height:9px;letter-spacing:2px}
.origin .flag{display:block;width:54px;height:26px;margin:2px auto 3px;background:linear-gradient(var(--flag-red) 0 15%,#fff 15% 30%,var(--flag-red) 30% 45%,#fff 45% 60%,var(--flag-red) 60% 75%,#fff 75% 88%,var(--flag-red) 88%)}
.cert{position:absolute;left:955px;top:316px;width:50px;text-align:center;font-size:8px;color:var(--grey)}
.cert .mark{width:44px;height:44px;border:2.5px solid #000;border-radius:50%;margin:0 auto 6px}
</style>
</head>
<body>
<main class="label">
  <div class="band g1"></div><div class="band b1"></div>
  <div class="band b2"></div><div class="band g2"></div>

  <section class="usage">
    <h2>Suggested Usage:</h2>
    <p>Lorem Ipsum. Proin gravida nibh vel velit auctor aliquet. Aenean sollicitudin, lorem quis bibendum auctor, nisi elit consequat ipsum, nec sagittis sem nibh id elit. Duis sed odio sit amet nibh vulputate cursus a sit amet mauris. Morbi accumsan ipsum velit. Nam nec tellus a odio tincidunt auctor a ornare odio. Sed non mauris vitae erat consequat auctor eu in elit.</p>
    <p class="note">Class aptent taciti sociosqu ad litora torquent per conubia nostra, per inceptos himenaeos. Mauris in erat justo. Nullam ac urna eu felis dapibus condimentum sit amet a augue. Sed non neque elit. Sed ut imperdiet nisi.</p>
    <p>Lorem Ipsum. Proin gravida nibh vel velit auctor aliquet. Aenean sollicitudin, lorem quis bibendum auctor, nisi elit consequat ipsum, nec sagittis sem nibh id elit. Duis sed odio sit amet nibh vulputate cursus a sit amet mauris.</p>
  </section>

  <div class="badges">
    <div class="badge"><div class="mark sq"></div>GMO Free</div>
    <div class="badge"><div class="mark"></div>Certified Organic</div>
    <div class="badge"><div class="mark"></div>Gluten Free</div>
    <div class="badge"><div class="mark sq"></div>Sugar Free</div>
  </div>

  <div class="brand-name">Lumorra</div>
  <div class="sun" role="img" aria-label="Illustrated rising sun with swirl centre"></div>

  <section class="product">
    <h1>Vita-Restore</h1>
    <div class="sub">Men’s Multi-Vitamen</div>
    <p class="desc">Lorem Ipsum. Proin gravida nibh<br>vel velit auctor aliquet.</p>
    <span class="pill">90 CAPSULES • DIETARY SUPPLEMENT</span>
  </section>

  <section class="facts">
    <div class="inner">
      <h3>Supplement Facts</h3>
      <div class="serv">Serving Size: 1 Packet (15 g) • Servings Per Container: 1</div>
      <table>
        <tr class="hd thick"><td></td><td class="n">Amount per Serving</td><td class="p">%DV*</td></tr>
        <tr><td class="b">Calories</td><td class="n">40</td><td class="p">**</td></tr>
        <tr class="thick"><td class="in">Calories from Fat</td><td class="n">0</td><td class="p">**</td></tr>
        <tr><td class="b">Total Fat</td><td class="n">0 g</td><td class="p">0</td></tr>
        <tr><td class="in">Saturated Fat</td><td class="n">0 g</td><td class="p">0</td></tr>
        <tr><td class="b">Sodium</td><td class="n">18 mg</td><td class="p">&lt;1%</td></tr>
        <tr><td class="b">Potassium</td><td class="n">395 mg</td><td class="p">11%</td></tr>
        <tr><td class="b">Total Carbohydrate</td><td class="n">9 g</td><td class="p">3%</td></tr>
        <tr><td class="in">Dietary Fiber</td><td class="n">1 g</td><td class="p">4%</td></tr>
        <tr><td class="in">Sugars</td><td class="n">7 g</td><td class="p">**</td></tr>
        <tr class="thick"><td class="b">Protein</td><td class="n">&lt;1 g</td><td class="p">1%</td></tr>
        <tr><td>Vitamin A</td><td class="n">0 g</td><td class="p">&lt;1%</td></tr>
        <tr><td>Vitamin C <small>(as ascorbic acid)</small></td><td class="n">60 mg</td><td class="p">100%</td></tr>
        <tr><td>Vitamin B3 <small>(as niacinamide)</small></td><td class="n">20 mg</td><td class="p">100%</td></tr>
        <tr><td>Vitamin B6 <small>(as pyroxodine HCl)</small></td><td class="n">2 mg</td><td class="p">100%</td></tr>
        <tr class="thick"><td>Vitamin B12</td><td class="n">6 mcg</td><td class="p">100%</td></tr>
      </table>
      <div class="foot">* % Daily Values (DV) based on a 2,000 Calorie diet. Your daily values may be higher or lower depending on your calorie needs.<br>** Daily Value not established.</div>
    </div>
  </section>

  <div class="origin"><span>MADE IN</span><span class="flag" role="img" aria-label="Striped national flag"></span><span>U. S. A.</span></div>
  <div class="cert"><div class="mark"></div>Certified</div>
</main>
</body>
</html>
```